Corvane Partners is a boutique consultancy focused on CXO-level advisory on strategy, operations, and organization in the Consumer Packaged Goods and Retail sector.

Our typical clients are senior level executives (Typically SVP level or higher), who hire us to help solve strategic business challenges. Our consultants are typically charged out at very high rates (Typically $2,000 - $3,000 per day), therefore, our business cards need to convey a high end, classy, yet professional image, consistent with high value strategic consulting.

We would like to see designs and colors that convey excellence, competence, and growth.

Our name 'Corvane' is derived from the Native American name of Mt. McKinley, the highest peak in North America. We would like to have a logo on our business card, that is simple yet conveys the aspirational nature of what we offer, i.e enabling the achievement of high performance.

Boutique

Corvane Partners, LLC
4417 Hollister Avenue Northwest, Suite 620
Washington, District of Columbia, 20016
United States
Mobile: +1 202 555 0148
ilsa.brenner@corvanepartnersllc.example

```html
<!DOCTYPE html>
<html lang="en">
<head>
<meta charset="utf-8">
<title>Corvane Partners, LLC — Business Card</title>
<link rel="stylesheet" href="https://fonts.googleapis.com/css2?family=Open+Sans:wght@400;600;700&display=swap">
<style>
  :root {
    --backdrop: #3b302b;
    --card-black: #0d0d0d;
    --card-black-edge: #1a1a1a;
    --paper-white: #f2f2f2;
    --ink-white: #ececec;
    --ink-black: #111111;
    --rule-grey: #8a8a8a;
    --gloss-grey: #4a4a4a;
  }
  * { box-sizing: border-box; margin: 0; padding: 0; }
  html, body {
    width: 1200px;
    height: 716px;
    overflow: hidden;
    background: var(--backdrop);
    font-family: "Open Sans", Arial, sans-serif;
  }
  .stage {
    position: relative;
    width: 1200px;
    height: 716px;
    display: flex;
    align-items: center;
    justify-content: center;
    gap: 60px;
  }
  .card {
    position: relative;
    width: 500px;
    height: 290px;
    background: var(--card-black);
    border: 1px solid var(--card-black-edge);
    box-shadow: 0 14px 30px rgba(0, 0, 0, 0.45);
    overflow: hidden;
  }

  /* Front */
  .card-front .brand {
    position: absolute;
    top: 38px;
    left: 0;
    right: 0;
    display: flex;
    flex-direction: column;
    align-items: center;
  }
  .card-front .brand-square {
    width: 18px;
    height: 18px;
    background: var(--ink-white);
    margin-bottom: 12px;
  }
  .card-front .brand-name {
    color: var(--ink-white);
    font-weight: 700;
    font-size: 24px;
    letter-spacing: 0.2px;
  }
  .card-front .brand-rule {
    width: 250px;
    height: 1px;
    background: var(--rule-grey);
    margin-top: 6px;
  }
  .card-front .name-band {
    position: absolute;
    top: 122px;
    left: 0;
    right: 0;
    height: 38px;
    background: var(--paper-white);
    display: flex;
    align-items: center;
    justify-content: center;
  }
  .card-front .person-name {
    color: var(--ink-black);
    font-weight: 700;
    font-size: 17px;
    padding-left: 40px;
  }
  .card-front .contact {
    position: absolute;
    top: 172px;
    left: 0;
    right: 0;
    text-align: center;
    color: var(--ink-white);
    font-size: 12px;
    line-height: 19px;
  }
  .card-front .contact-rule {
    width: 290px;
    height: 1px;
    background: var(--rule-grey);
    margin: 4px auto;
  }
  .card-front .contact-rule.wide { width: 400px; }

  /* Back */
  .card-back {
    display: flex;
    align-items: center;
    justify-content: center;
  }
  .card-back .brand {
    display: flex;
    flex-direction: column;
    align-items: center;
  }
  .card-back .brand-square {
    width: 34px;
    height: 34px;
    background: var(--gloss-grey);
    margin-bottom: 16px;
  }
  .card-back .brand-name {
    color: var(--gloss-grey);
    font-weight: 700;
    font-size: 34px;
    letter-spacing: 0.2px;
  }
  .card-back .brand-rule {
    width: 330px;
    height: 1px;
    background: var(--gloss-grey);
    margin-top: 8px;
  }
</style>
</head>
<body>
  <main class="stage">
    <section class="card card-front" aria-label="Business card front">
      <div class="brand">
        <span class="brand-square" aria-hidden="true"></span>
        <span class="brand-name">Corvane Partners, LLC</span>
        <span class="brand-rule"></span>
      </div>
      <div class="name-band">
        <span class="person-name">Ilsa Brenner</span>
      </div>
      <div class="contact">
        <p class="contact-phone">[C]: +1 202 555 0148</p>
        <p class="contact-email">[E]: ilsa.brenner@corvanepartnersllc.example</p>
        <div class="contact-rule"></div>
        <p class="contact-address">4417 Hollister Avenue Northwest,</p>
        <p class="contact-address">Suite 620 Washington, District of Columbia, 20016 United States</p>
        <div class="contact-rule wide"></div>
      </div>
    </section>

    <section class="card card-back" aria-label="Business card back">
      <div class="brand">
        <span class="brand-square" aria-hidden="true"></span>
        <span class="brand-name">Corvane Partners, LLC</span>
        <span class="brand-rule"></span>
      </div>
    </section>
  </main>
</body>
</html>
```